Tamsen Health Guides
Your Personal Medical Record
Tamsen Health Guides - Medical
Creative Brief
Professional
Gareth L. Pomroy
MD
4271 Copper Finch Avenue Denver, Colorado 80219
garethlpomroy@mailvessel.example
mytamsen.example
I need the business card to include the scan icon for smart phone users to access the website from the business card.
SiteAdmin SiteAdmin

```html
<!DOCTYPE html>
<html lang="en">
<head>
<meta charset="utf-8">
<title>Tamsen Health Guides – Business Card</title>
<link href="https://fonts.googleapis.com/css2?family=Open+Sans:wght@400;600;700&display=swap" rel="stylesheet">
<style>
  :root {
    --bg: #e9e9ec;
    --paper: #ffffff;
    --violet-dark: #1f1470;
    --violet: #2e22a6;
    --violet-light: #4a3fd0;
    --stripe: #8d8d93;
    --ink-light: #ffffff;
    --ink-soft: #d9d6f5;
    --brand-ink: #2a2198;
    --brand-sub: #6d6d74;
  }
  * { box-sizing: border-box; margin: 0; padding: 0; }
  html, body { width: 1200px; height: 901px; overflow: hidden; }
  body {
    background: var(--bg);
    font-family: "Open Sans", Arial, sans-serif;
    position: relative;
  }
  .card {
    position: absolute;
    left: 250px;
    width: 700px;
    height: 400px;
    border-radius: 22px;
    overflow: hidden;
    box-shadow: 0 6px 18px rgba(0,0,0,.18);
  }
  .card--back { top: 40px; background: linear-gradient(135deg, var(--violet-light), var(--violet) 45%, var(--violet-dark)); }
  .card--front { top: 461px; background: var(--paper); display: flex; }

  .back-brand {
    position: absolute; left: 0; right: 0; top: 110px;
    display: flex; flex-direction: column; align-items: center; gap: 14px;
    padding-right: 90px;
  }
  .back-brand__name { color: var(--ink-light); font-weight: 700; font-size: 40px; letter-spacing: .5px; }
  .back-brand__url { color: var(--ink-soft); font-size: 18px; letter-spacing: 1px; align-self: flex-end; margin-right: 150px; }

  .front-brand {
    width: 52%;
    display: flex; flex-direction: column; justify-content: center; align-items: center; gap: 8px;
    padding: 0 10px 30px 20px;
  }
  .front-brand__name { color: var(--brand-ink); font-weight: 700; font-size: 29px; white-space: nowrap; }
  .front-brand__tagline { color: var(--brand-sub); font-weight: 700; font-size: 15px; letter-spacing: .6px; white-space: nowrap; }

  .divider { width: 14px; background: linear-gradient(90deg, #b5b5ba, var(--stripe)); margin-left: 10px; }

  .contact {
    flex: 1;
    background: linear-gradient(135deg, var(--violet-light), var(--violet) 50%, var(--violet-dark));
    color: var(--ink-light);
    padding: 88px 16px 0 26px;
    font-size: 13.5px;
  }
  .contact__name { font-weight: 700; font-size: 17px; }
  .contact__title { font-size: 13px; margin-bottom: 22px; color: var(--ink-soft); }
  .contact__address { line-height: 1.45; margin-bottom: 16px; }
  .contact__row { display: flex; align-items: center; gap: 10px; line-height: 1.7; white-space: nowrap; }
  .contact__row svg { width: 14px; height: 14px; flex: none; }
</style>
</head>
<body>
  <section class="card card--back">
    <div class="back-brand">
      <div class="back-brand__name">Tamsen Health Guides</div>
      <div class="back-brand__url">mytamsen.example</div>
    </div>
  </section>

  <section class="card card--front">
    <div class="front-brand">
      <div class="front-brand__name">Tamsen Health Guides</div>
      <div class="front-brand__tagline">Your Personal Medical Records</div>
    </div>
    <div class="divider"></div>
    <div class="contact">
      <div class="contact__name">Gareth L. Pomroy</div>
      <div class="contact__title">MD</div>
      <div class="contact__address">4271 Copper Finch Avenue<br>Denver, Colorado 80219</div>
      <div class="contact__row">
        <svg viewBox="0 0 16 16"><path fill="#fff" d="M3 1h3l1.5 4-2 1.3a9 9 0 0 0 4.2 4.2L11 8.5l4 1.5v3c0 1-1 2-2 2C6.4 15 1 9.6 1 3c0-1 1-2 2-2z"/></svg>
        <span>303-555-0148</span>
      </div>
      <div class="contact__row">
        <svg viewBox="0 0 16 16"><rect x="1" y="3" width="14" height="10" rx="1" fill="none" stroke="#fff" stroke-width="1.5"/><path d="M1.5 3.5 8 9l6.5-5.5" fill="none" stroke="#fff" stroke-width="1.5"/></svg>
        <span>garethlpomroy@mailvessel.example</span>
      </div>
      <div class="contact__row">
        <svg viewBox="0 0 16 16"><circle cx="8" cy="8" r="6.5" fill="none" stroke="#fff" stroke-width="1.4"/><ellipse cx="8" cy="8" rx="3" ry="6.5" fill="none" stroke="#fff" stroke-width="1.2"/><path d="M1.5 8h13" stroke="#fff" stroke-width="1.2"/></svg>
        <span>mytamsen.example</span>
      </div>
    </div>
  </section>
</body>
</html>
```